Our companies name is The Gilded Ladle and we specialize in craft cupcakes, what I mean by that is that we bake our cupcakes with craft beer and other alcoholic drinks. We are trying to focus on being elegant but at the same time unpretentious. Since we are incorporating beer in our cupcakes we want the business card to have our logo in the front and our information in the back.

Once we select the best design we will provide the contact information to be added. Thank you.

Industry/Entity Type

Business

Font styles to use
Decorative
Script

Requirements
Must have
• Round corners
Should not have
• Square corners

```html
<!DOCTYPE html>
<html lang="en">
<head>
<meta charset="utf-8">
<title>The Gilded Ladle – Business Card</title>
<link rel="stylesheet" href="https://fonts.googleapis.com/css2?family=Great+Vibes&family=Roboto+Slab:wght@700&family=Lato:wght@400;700&display=swap">
<style>
  :root {
    --backdrop: #7a4317;
    --card: #0d0d0f;
    --card-edge: #1c1c20;
    --teal: #7fd1c2;
    --red: #e23b40;
    --white: #f4f4f4;
    --muted: #d9d9d9;
  }
  * { box-sizing: border-box; margin: 0; padding: 0; }
  html, body { width: 1200px; height: 913px; overflow: hidden; }
  body {
    background: var(--backdrop);
    position: relative;
    font-family: "Lato", sans-serif;
  }
  .card {
    position: absolute;
    top: 302px;
    width: 540px;
    height: 309px;
    border-radius: 26px;
    background: linear-gradient(135deg, var(--card-edge) 0%, var(--card) 55%);
    border: 3px solid var(--white);
    box-shadow: 0 18px 30px rgba(0,0,0,0.35);
    overflow: hidden;
  }
  .card--front { left: 40px; }
  .card--back { left: 620px; }

  .brand {
    display: flex;
    align-items: center;
    gap: 14px;
    font-family: "Roboto Slab", serif;
    font-weight: 700;
    color: var(--teal);
    text-transform: uppercase;
    letter-spacing: 2px;
  }
  .brand__dot {
    width: 16px; height: 16px;
    border-radius: 50%;
    background: var(--red);
    flex: none;
  }
  .card--front .brand {
    position: absolute;
    left: 50%; top: 50%;
    transform: translate(-50%, -50%);
    font-size: 38px;
    white-space: nowrap;
  }
  .card--back .brand {
    position: absolute;
    left: 200px; top: 168px;
    font-size: 22px;
    white-space: nowrap;
  }

  .people {
    position: absolute;
    right: 30px; top: 18px;
    text-align: right;
  }
  .person__name {
    font-family: "Great Vibes", cursive;
    color: var(--teal);
    font-size: 40px;
    line-height: 1;
  }
  .person__role {
    font-family: "Roboto Slab", serif;
    font-weight: 700;
    font-size: 12px;
    color: var(--white);
    margin: 2px 20px 8px 0;
  }

  .contact {
    position: absolute;
    left: 26px; bottom: 22px;
    list-style: none;
    color: var(--white);
    font-size: 16px;
  }
  .contact__item {
    display: flex;
    align-items: center;
    gap: 10px;
    margin-top: 6px;
  }
  .contact__icon { width: 18px; height: 18px; flex: none; }
</style>
</head>
<body>

<section class="card card--front" aria-label="Card front">
  <div class="brand"><span class="brand__dot"></span>The Gilded Ladle</div>
</section>

<section class="card card--back" aria-label="Card back">
  <div class="people">
    <p class="person__name">Elena Marsh</p>
    <p class="person__role">Owner</p>
    <p class="person__name">Rafael Ortiz</p>
    <p class="person__role">Co-Owner</p>
  </div>

  <div class="brand"><span class="brand__dot"></span>The Gilded Ladle</div>

  <ul class="contact">
    <li class="contact__item">
      <svg class="contact__icon" viewBox="0 0 18 18" aria-hidden="true">
        <rect x="1.5" y="1.5" width="15" height="15" rx="2" fill="none" stroke="#7fd1c2" stroke-width="1.5"/>
        <path d="M6 5 L8 5 L9 7.5 L7.8 8.5 Q8.8 10.5 10.5 11.2 L11.5 10 L13.5 11 L13.5 13 Q9 13.5 6 10 Q4.8 7.5 6 5 Z" fill="#7fd1c2"/>
      </svg>
      <span>555-214-8830</span>
    </li>
    <li class="contact__item">
      <svg class="contact__icon" viewBox="0 0 18 18" aria-hidden="true">
        <rect x="1.5" y="1.5" width="15" height="15" rx="2" fill="#7fd1c2"/>
        <path d="M3.5 5 L9 10 L14.5 5 M3.5 13 L7.5 8.5 M14.5 13 L10.5 8.5" fill="none" stroke="#0d0d0f" stroke-width="1.4"/>
      </svg>
      <span>hello@gildedladle.com</span>
    </li>
  </ul>
</section>

</body>
</html>
```